Website Creation for Bloom Course 2025 by Otto Varsk "The Woman Who Walked the Tideline"

Project Title: "Bloom" Course Design Brief – Website design Build on Tilda
Client: Pinecrest Lantern Education
Course Title: Bloom by Otto Varsk – The Woman Who Walked the Tideline
Logo: Otto Varsk Logo
Course price: TBA
Overview:
We are seeking a designer to create cohesive and professional design assets for a new online course called Bloom. This transformative program combines neuroscience, emotional wellness, and ancient meditation practices to guide users through a journey of self-healing. We want the design to feel scientific yet spiritual, with clean, modern aesthetics that also convey depth and transformation. We use Tilda as our website builder so we need a design that can be easily transposed to that platform.
We require a visually compelling and dynamic banner image for the course webpage hero section (desktop and mobile versions)
We also require 7 x Individual thumbnail designs for each chakra meditation that will accompany the course with a workbook that will be designed in house (aligned with energy centre themes / Solfeggio frequencies / cosmic and sacred geometry)
Visual Direction:
• Clean, modern design with dark elements that balance science and spirituality.
• Soft gradients, energetic colors for chakras, and subtle abstract patterns or sacred geometry.
• Imagery could include brain neural networks, energy centres, or serene meditative figures and sacred geometry.
Course Themes to Inspire Design:
• Neuroplasticity and brain rewiring
• Emotional trauma and healing
• Meditation and Solfeggio frequencies
• Mind-body-spirit connection
• Empowerment and transformation
Lesson Breakdown:
• Lesson 1: The Science of Meditation & the Mind-Body Connection
• Lesson 2: Otto Varsk’s Personal Healing & Neuroplasticity
• Lesson 3: Emotional Stress and Disease
• Lesson 4: VLR (Velvet Lattice Reset) Process
• Lesson 5: Solfeggio Frequencies & Chakra Healing
Target Audience:
Adult women 40 to 60 years old interested in healing illness, improving mental health, improving relationships, improving personal development, alternative healing, and meditation.

self development, meditation, healing

1 page

• futurapt

• branding copy used with relevant imagery and brand colours Stone #FAF0EA Sand #E2B9A5 Steel Blue #4F5266 Navy #2B243A Black: #000000 and Futura PT font
• chakra symbols and cosmic aesthetics with informational psychographics
• bright bold colours that don't match our branding

```html
<!DOCTYPE html>
<html lang="en">
<head>
<meta charset="utf-8">
<title>Bloom by Otto Varsk</title>
<link href="https://fonts.googleapis.com/css2?family=Montserrat:wght@300;400;500;600;700;800&display=swap" rel="stylesheet">
<style>
:root{
  --navy:#100c45;
  --navy-deep:#0b0940;
  --ink:#111111;
  --text:#333333;
  --orange:#f58220;
  --cyan:#2ee8e6;
  --pale:#eef3f8;
  --card-grey:#f3f2f4;
  --white:#ffffff;
  --root-bg:#fde3e3;--root:#d8151b;
  --sacral-bg:#fbe6d4;--sacral:#e2640f;
  --solar-bg:#fdf1bd;--solar:#d4a80a;
  --heart-bg:#d9fbd6;--heart:#20a12a;
  --l1:#2ee6e6;--l2:#4bb27a;--l3:#7a3fa0;--l4:#f58220;--l5:#e53935;
}
*{margin:0;padding:0;box-sizing:border-box}
html,body{width:1200px;height:4112px;overflow:hidden}
body{position:relative;font-family:'Montserrat',sans-serif;color:var(--text);background:var(--white)}
.abs{position:absolute}
.section-title{position:absolute;left:0;width:1200px;text-align:center;font-weight:800;color:var(--ink);font-size:34px;line-height:42px;text-transform:uppercase}
.rule{position:absolute;height:3px;background:var(--orange)}

/* hero */
.hero{position:absolute;left:0;top:0;width:1200px;height:655px;background:linear-gradient(100deg,#0f0b42 0%,#150d4c 50%,#1a0f52 100%);overflow:hidden}
.hero-visual{position:absolute;left:590px;top:40px;width:610px;height:615px;
  background:
    radial-gradient(ellipse 42% 30% at 62% 30%,rgba(255,120,200,.85) 0%,rgba(190,70,220,.55) 40%,rgba(90,40,190,0) 100%),
    radial-gradient(ellipse 30% 48% at 40% 62%,rgba(40,150,255,.75) 0%,rgba(40,90,220,.35) 55%,rgba(20,20,120,0) 100%),
    radial-gradient(ellipse 60% 60% at 55% 45%,rgba(110,50,200,.55) 0%,rgba(16,12,69,0) 75%)}
.hero-edge{position:absolute;left:0;top:651px;width:1200px;height:4px;background:repeating-linear-gradient(90deg,var(--white) 0 4px,transparent 4px 8px)}
.logo{position:absolute;left:140px;top:84px;width:140px;text-align:center;color:var(--white);font-weight:500;font-size:14px;letter-spacing:3px;white-space:nowrap}
.nav a{position:absolute;top:32px;height:32px;line-height:32px;font-size:13px;color:var(--white);text-decoration:none;white-space:nowrap}
.nav a.active{background:var(--orange);padding:0 12px}
.hero-kicker{position:absolute;left:146px;top:190px;font-size:56px;line-height:64px;font-weight:800;color:var(--white)}
.hero-sub{position:absolute;left:148px;top:264px;font-size:42px;font-weight:400;line-height:50px;color:var(--white);white-space:nowrap}
.hero-price{position:absolute;left:148px;top:428px;font-size:56px;line-height:68px;font-weight:800;color:var(--orange)}
.btn-start{position:absolute;left:152px;top:522px;width:201px;height:57px;background:var(--cyan);color:var(--navy-deep);font-weight:800;font-size:20px;line-height:57px;text-align:center}

/* workbooks */
.arrow{position:absolute;width:40px;height:40px;border:1.5px solid #b9b9b9;border-radius:50%;background:var(--white)}
.arrow svg{position:absolute;left:11px;top:11px}
.wb-card{position:absolute;top:823px;width:214px;height:339px;text-align:center}
.wb-name{position:absolute;top:26px;width:100%;font-size:18px;font-weight:700}
.wb-theme{position:absolute;top:54px;width:100%;font-size:11px;color:#333}
.wb-symbol{position:absolute;left:38px;top:102px;width:138px;height:138px;border-radius:50%;box-shadow:inset 0 -8px 18px rgba(0,0,0,.18)}
.wb-text{position:absolute;top:277px;width:100%;font-size:12px;line-height:19px;color:#333}

/* benefits */
.benefits{position:absolute;left:0;top:1221px;width:1200px;height:649px;background:var(--pale)}
.benefit{position:absolute;left:193px;font-size:15px;font-weight:600;line-height:22px;color:#222;width:330px}
.benefit-icon{position:absolute;left:154px;width:22px;height:22px}
.figure{position:absolute;left:539px;top:1280px;width:514px;height:540px;
  background:linear-gradient(#d486d6 0%,#7b5fdc 14%,#4a6be6 26%,#2ab3e6 38%,#3fcb9a 50%,#d2d43a 62%,#f6a624 76%,#ef5a34 90%,#e9413a 100%);
  -webkit-mask-image:radial-gradient(ellipse 50% 50% at 50% 50%,#000 55%,transparent 100%);
  mask-image:radial-gradient(ellipse 50% 50% at 50% 50%,#000 55%,transparent 100%)}

/* lessons */
.lesson-visual{position:absolute;left:153px;top:2041px;width:493px;height:466px;background:radial-gradient(ellipse 45% 55% at 50% 48%,#9be4ff 0%,#3a8ee8 25%,#1a4cb4 50%,#0c2466 75%,#060b30 100%)}
.lesson-badge{position:absolute;left:774px;height:19px;line-height:19px;padding:0 6px;font-size:12px;font-weight:600;color:var(--white)}
.lesson-title{position:absolute;left:774px;font-size:16px;font-weight:600;line-height:21px;color:#222}
.lesson-icon{position:absolute;left:700px;width:52px;height:52px}

/* worth */
.worth{position:absolute;left:0;top:2573px;width:1200px;height:551px;background:var(--pale);overflow:hidden}
.worth-tint{position:absolute;width:260px;height:260px;border-radius:50%;background:radial-gradient(circle,rgba(240,170,200,.35),rgba(240,170,200,0) 70%)}
.worth-lead{position:absolute;left:250px;top:2682px;width:700px;text-align:center;font-size:13px;line-height:21px;color:#333}
.feat-circle{position:absolute;top:2791px;width:112px;height:112px;border-radius:50%}
.feat-circle svg{position:absolute;left:36px;top:36px}
.feat-title{position:absolute;top:2938px;width:280px;text-align:center;font-size:19px;font-weight:500;color:#222}
.feat-text{position:absolute;top:2980px;width:270px;text-align:center;font-size:13px;line-height:21px;color:#333}

/* testimonial */
.quote-box{position:absolute;left:150px;top:3347px;width:898px;height:332px;background:var(--card-grey)}
.avatar{position:absolute;left:213px;top:3431px;width:158px;height:158px;border-radius:50%;background:linear-gradient(#c9c3ba 0%,#b59a7c 55%,#8d7358 100%)}
.quote-mark{position:absolute;left:434px;top:3378px;font-size:72px;font-weight:800;color:var(--navy);line-height:72px}
.quote-text{position:absolute;left:434px;top:3443px;width:540px;font-size:13px;line-height:21px;color:#333}
.quote-name{position:absolute;left:439px;top:3624px;font-size:13px;font-weight:700;color:#222}

/* footer */
.footer{position:absolute;left:0;top:3743px;width:1200px;height:369px;background:var(--navy-deep)}
.footer-logo{position:absolute;left:142px;top:3874px;width:198px;text-align:center;font-size:22px;font-weight:500;letter-spacing:4px;color:var(--white);white-space:nowrap}
.foot-head{position:absolute;top:3786px;font-size:13px;font-weight:800;color:var(--white)}
.foot-link{position:absolute;left:402px;font-size:13px;color:var(--white)}
.foot-info{position:absolute;left:631px;font-size:13px;line-height:22px;color:var(--white)}
.foot-ico{position:absolute;left:608px}
.social{position:absolute;top:3845px;width:32px;height:32px;border-radius:50%;background:var(--white)}
.divider{position:absolute;left:148px;top:4025px;width:900px;height:1px;background:#5a5890}
.copyright{position:absolute;left:0;top:4065px;width:1200px;text-align:center;font-size:11px;color:#c9c8e0}
</style>
</head>
<body>

<section class="hero">
  <div class="hero-visual" role="img" aria-label="Glowing neural brain inside a meditating woman's head silhouette"></div>
  <div class="hero-edge"></div>
  <div class="logo">OTTO VARSK</div>
  <nav class="nav">
    <a class="active" style="left:490px">HOME</a>
    <a style="left:583px">ABOUT US</a>
    <a style="left:688px">LESSONS</a>
    <a style="left:784px">SERVICES</a>
    <a style="left:887px">BLOG</a>
    <a style="left:958px">CONTACT US</a>
  </nav>
  <div class="hero-kicker">BLOOM</div>
  <div class="hero-sub">Bloom by Otto Varsk –<br>The Woman Who Walked<br>the Tideline</div>
  <div class="hero-price">AUD 4999</div>
  <div class="btn-start">GET STARTED</div>
</section>

<h2 class="section-title" style="top:703px">Workbooks</h2>
<div class="rule" style="left:570px;top:771px;width:61px"></div>

<div class="arrow" style="left:69px;top:973px"><svg width="16" height="16" viewBox="0 0 16 16"><path d="M10 3 5 8l5 5" fill="none" stroke="#999" stroke-width="1.5"/></svg></div>
<div class="arrow" style="left:1083px;top:973px"><svg width="16" height="16" viewBox="0 0 16 16"><path d="M6 3l5 5-5 5" fill="none" stroke="#999" stroke-width="1.5"/></svg></div>

<div class="wb-card" style="left:150px;background:var(--root-bg)">
  <div class="wb-name" style="color:var(--root)">Root Chakra</div>
  <div class="wb-theme">Grounding &amp; Stability</div>
  <div class="wb-symbol" role="img" aria-label="Root chakra symbol" style="background:radial-gradient(circle at 45% 40%,#ef3a40,#b8121a 60%,#8c0a10)"></div>
  <div class="wb-text">Lorem Ipsum is simply<br>dummy text of th typesettin</div>
</div>
<div class="wb-card" style="left:378px;background:var(--sacral-bg)">
  <div class="wb-name" style="color:var(--sacral)">Sacral Chakra</div>
  <div class="wb-theme">Creativity &amp; Flow</div>
  <div class="wb-symbol" role="img" aria-label="Sacral chakra symbol" style="background:radial-gradient(circle at 45% 40%,#f7902a,#c84d0e 60%,#9a360a)"></div>
  <div class="wb-text">Lorem Ipsum is simply<br>dummy text of th typesettin</div>
</div>
<div class="wb-card" style="left:606px;background:var(--solar-bg)">
  <div class="wb-name" style="color:var(--solar)">Solar Plexus Chakra</div>
  <div class="wb-theme">Confidence &amp; Power</div>
  <div class="wb-symbol" role="img" aria-label="Solar plexus chakra symbol" style="background:radial-gradient(circle at 45% 40%,#f5cf2a,#c29a08 60%,#98780a)"></div>
  <div class="wb-text">Lorem Ipsum is simply<br>dummy text of th typesettin</div>
</div>
<div class="wb-card" style="left:835px;background:var(--heart-bg)">
  <div class="wb-name" style="color:var(--heart)">Heart Chakra</div>
  <div class="wb-theme">Love &amp; Compassion</div>
  <div class="wb-symbol" role="img" aria-label="Heart chakra symbol" style="background:radial-gradient(circle at 45% 40%,#36c43e,#15901c 60%,#0c6c12)"></div>
  <div class="wb-text">Lorem Ipsum is simply<br>dummy text of th typesettin</div>
</div>

<section class="benefits"></section>
<h2 class="abs" style="left:155px;top:1272px;font-size:31px;line-height:42px;font-weight:800;color:var(--ink)">WHAT WILL I GET FROM<br>THE HEALING COURSE?</h2>
<div class="rule" style="left:155px;top:1375px;width:59px"></div>

<svg class="benefit-icon" style="top:1430px" viewBox="0 0 22 22"><circle cx="11" cy="11" r="10" fill="none" stroke="#222" stroke-width="1.4"/><path d="M9 7l4 4-4 4" fill="none" stroke="#222" stroke-width="1.4"/></svg>
<div class="benefit" style="top:1422px">You will learn easy methods to manage pain on your own</div>
<svg class="benefit-icon" style="top:1503px" viewBox="0 0 22 22"><circle cx="11" cy="11" r="10" fill="none" stroke="#222" stroke-width="1.4"/><path d="M9 7l4 4-4 4" fill="none" stroke="#222" stroke-width="1.4"/></svg>
<div class="benefit" style="top:1494px">You will learn the basic body functions and its processes</div>
<svg class="benefit-icon" style="top:1577px" viewBox="0 0 22 22"><circle cx="11" cy="11" r="10" fill="none" stroke="#222" stroke-width="1.4"/><path d="M9 7l4 4-4 4" fill="none" stroke="#222" stroke-width="1.4"/></svg>
<div class="benefit" style="top:1571px">You will find out how to improve your body functions through diet</div>
<svg class="benefit-icon" style="top:1657px" viewBox="0 0 22 22"><circle cx="11" cy="11" r="10" fill="none" stroke="#222" stroke-width="1.4"/><path d="M9 7l4 4-4 4" fill="none" stroke="#222" stroke-width="1.4"/></svg>
<div class="benefit" style="top:1650px">You will gain self-healing skills through breath and touch</div>
<svg class="benefit-icon" style="top:1737px" viewBox="0 0 22 22"><circle cx="11" cy="11" r="10" fill="none" stroke="#222" stroke-width="1.4"/><path d="M9 7l4 4-4 4" fill="none" stroke="#222" stroke-width="1.4"/></svg>
<div class="benefit" style="top:1730px">You will learn easy methods of independent body work that will make you feel better everyday</div>

<div class="figure" role="img" aria-label="Rainbow meditating figure with seven chakra symbols"></div>

<h2 class="section-title" style="top:1921px">Lessons</h2>
<div class="rule" style="left:571px;top:1987px;width:59px"></div>
<div class="lesson-visual" role="img" aria-label="Glowing meditating figure inside a cosmic energy sphere"></div>

<svg class="lesson-icon" style="top:2033px" viewBox="0 0 52 52" fill="none" stroke="var(--l1)" stroke-width="1.6"><circle cx="26" cy="22" r="15"/><circle cx="26" cy="22" r="6"/><path d="M18 36v10M34 36v10"/></svg>
<div class="lesson-badge" style="top:2040px;background:var(--l1);color:#0b0940">LESSON 1</div>
<div class="lesson-title" style="top:2071px;width:270px">The Science of Meditation &amp; the Mind-Body Connection</div>

<svg class="lesson-icon" style="top:2138px" viewBox="0 0 52 52" fill="none" stroke="var(--l2)" stroke-width="1.6"><path d="M26 30V12M26 20c-8 0-10-6-10-8 6 0 10 2 10 8zM26 18c6 0 9-5 9-8-6 0-9 3-9 8z"/><path d="M4 38c8-4 14-4 22 0h14"/></svg>
<div class="lesson-badge" style="top:2144px;background:var(--l2)">LESSON 2</div>
<div class="lesson-title" style="top:2174px;width:250px">Otto Varsk’s Personal Healing &amp; Neuroplasticity</div>

<svg class="lesson-icon" style="top:2240px" viewBox="0 0 52 52" fill="none" stroke="var(--l3)" stroke-width="1.6"><circle cx="26" cy="18" r="5"/><path d="M14 42c2-10 6-16 12-16s10 6 12 16z"/><path d="M8 10l4 4M44 10l-4 4M26 4v5"/></svg>
<div class="lesson-badge" style="top:2246px;background:var(--l3)">LESSON 3</div>
<div class="lesson-title" style="top:2275px;width:270px">Emotional Stress and Disease</div>

<svg class="lesson-icon" style="top:2330px" viewBox="0 0 52 52" fill="none" stroke="var(--l4)" stroke-width="1.6"><ellipse cx="26" cy="26" rx="20" ry="8"/><ellipse cx="26" cy="26" rx="20" ry="8" transform="rotate(60 26 26)"/><ellipse cx="26" cy="26" rx="20" ry="8" transform="rotate(120 26 26)"/><circle cx="26" cy="26" r="3"/></svg>
<div class="lesson-badge" style="top:2331px;background:var(--l4)">LESSON 4</div>
<div class="lesson-title" style="top:2360px;width:230px">VLR (Velvet Lattice Reset) Process</div>

<svg class="lesson-icon" style="top:2440px" viewBox="0 0 52 52" fill="none" stroke="var(--l5)" stroke-width="1.6"><circle cx="26" cy="10" r="5"/><path d="M26 15v16M14 28l12-6 12 6M8 44c6-8 30-8 36 0z"/></svg>
<div class="lesson-badge" style="top:2439px;background:var(--l5)">LESSON 5</div>
<div class="lesson-title" style="top:2469px;width:220px">Solfeggio Frequencies &amp; Chakra Healing</div>

<section class="worth">
  <div class="worth-tint" role="img" aria-label="Faint mandala decoration" style="left:1040px;top:-20px"></div>
  <div class="worth-tint" role="img" aria-label="Faint mandala decoration" style="left:-120px;top:310px"></div>
</section>
<h2 class="section-title" style="top:2631px">Why is it worth it?</h2>
<p class="worth-lead">Lorem ipsum dolor sit amet, consectetur adipiscing elit, sed do eiusmod tempor incididunt ut labore et dolore magna aliqua. Ut enim ad minim veniam, quis nostrud exercitation ullamco</p>
<div class="rule" style="left:570px;top:2749px;width:61px"></div>

<div class="feat-circle" style="left:225px;background:#d6f7d6"><svg width="40" height="40" viewBox="0 0 40 40" fill="none" stroke="#2a9a3a" stroke-width="1.8"><rect x="4" y="6" width="32" height="22"/><path d="M2 32h36M10 14h10M10 20h6M24 16h8v8h-8z"/></svg></div>
<div class="feat-title" style="left:141px">5 Lessons</div>
<div class="feat-text" style="left:146px">Lorem ipsum dolor sit amet, consectetur adipiscing elit, sed do eiusmod tempor incididunt ut labore et dolore magna aliqua. Ut enim ad minim.</div>

<div class="feat-circle" style="left:542px;background:#fdf0b8"><svg width="40" height="40" viewBox="0 0 40 40" fill="none" stroke="#f0922a" stroke-width="2"><path d="M30 20v14H6V10h14"/><path d="M28 5l7 7-15 15h-7v-7z"/></svg></div>
<div class="feat-title" style="left:458px">Lorem Ipsum</div>
<div class="feat-text" style="left:463px">Lorem ipsum dolor sit amet, consectetur adipiscing elit, sed do eiusmod tempor incididunt ut labore et dolore magna aliqua. Ut enim ad minim.</div>

<div class="feat-circle" style="left:855px;background:#f0d9f0"><svg width="40" height="40" viewBox="0 0 40 40" fill="none" stroke="#8a4aa8" stroke-width="1.8"><rect x="4" y="6" width="32" height="22"/><path d="M14 34h12M20 28v6M10 12h10M10 18h14"/></svg></div>
<div class="feat-title" style="left:771px">Lorem Ipsum</div>
<div class="feat-text" style="left:776px">Lorem ipsum dolor sit amet, consectetur adipiscing elit, sed do eiusmod tempor incididunt ut labore et dolore magna aliqua. Ut enim ad minim.</div>

<h2 class="section-title" style="top:3180px">What other people<br>say about our courses</h2>
<div class="rule" style="left:570px;top:3296px;width:61px"></div>

<div class="arrow" style="left:69px;top:3486px"><svg width="16" height="16" viewBox="0 0 16 16"><path d="M10 3 5 8l5 5" fill="none" stroke="#999" stroke-width="1.5"/></svg></div>
<div class="arrow" style="left:1083px;top:3486px"><svg width="16" height="16" viewBox="0 0 16 16"><path d="M6 3l5 5-5 5" fill="none" stroke="#999" stroke-width="1.5"/></svg></div>

<div class="quote-box"></div>
<div class="avatar" role="img" aria-label="Portrait photo of the reviewer"></div>
<div class="quote-mark">“</div>
<p class="quote-text">Sed ut perspiciatis unde omnis iste natus error sit voluptatem accusantium doloremque laudantium, totam rem aperiam, eaque ipsa quae ab illo inventore veritatis et quasi architecto beatae vitae dicta sunt explicabo. Nemo enim ipsam voluptatem quia voluptas sit aspernatur aut odit aut fugit, sed quia conse quuntur magni dolores eos qui ratione voluptatem sequi nesciunt. Neque porro quisquam est, qui dolorem ipsum quia dolor sit ame</p>
<div class="rule" style="left:439px;top:3599px;width:45px"></div>
<div class="quote-name">LENA MORROW</div>

<footer class="footer"></footer>
<div class="footer-logo">OTTO VARSK</div>

<div class="foot-head" style="left:402px">MENU</div>
<div class="rule" style="left:402px;top:3816px;width:118px"></div>
<div class="foot-link" style="top:3843px">HOME</div>
<div class="foot-link" style="top:3865px">ABOUT US</div>
<div class="foot-link" style="top:3888px">LESSONS</div>
<div class="foot-link" style="top:3910px">SERVICES</div>
<div class="foot-link" style="top:3933px">BLOG</div>
<div class="foot-link" style="top:3955px">CONTACT US</div>

<div class="foot-head" style="left:610px">CONTACT US</div>
<div class="rule" style="left:610px;top:3816px;width:121px"></div>
<svg class="foot-ico" style="top:3846px" width="12" height="16" viewBox="0 0 12 16"><path d="M6 0a6 6 0 0 0-6 6c0 4.5 6 10 6 10s6-5.5 6-10a6 6 0 0 0-6-6zm0 8.5A2.5 2.5 0 1 1 6 3.5a2.5 2.5 0 0 1 0 5z" fill="#fff"/></svg>
<div class="foot-info" style="top:3840px">118 Harlow Lane<br>Brookfield, OR 97031</div>
<svg class="foot-ico" style="top:3913px" width="12" height="12" viewBox="0 0 24 24"><path d="M6.6 10.8a15 15 0 0 0 6.6 6.6l2.2-2.2c.3-.3.7-.4 1-.2 1.1.4 2.3.6 3.6.6.6 0 1 .4 1 1V20c0 .6-.4 1-1 1A17 17 0 0 1 3 4c0-.6.4-1 1-1h3.5c.6 0 1 .4 1 1 0 1.300.2 2.500.6 3.600.1.3 0 .7-.2 1z" fill="#fff"/></svg>
<div class="foot-info" style="top:3907px">+1 555 014 2290</div>
<svg class="foot-ico" style="top:3953px" width="13" height="10" viewBox="0 0 13 10"><rect width="13" height="10" rx="1" fill="#fff"/><path d="M0 1l6.5 5L13 1" fill="none" stroke="#0b0940" stroke-width="1.2"/></svg>
<div class="foot-info" style="top:3947px">info@ottovarsk.com</div>

<div class="foot-head" style="left:852px">FOLLOW US</div>
<div class="rule" style="left:852px;top:3816px;width:118px"></div>
<div class="social" style="left:849px"></div>
<div class="social" style="left:888px"></div>
<div class="social" style="left:927px"></div>
<div class="social" style="left:966px"></div>
<div class="social" style="left:1004px"></div>

<div class="divider"></div>
<div class="copyright">Copyright © 2025 All Rights Reserved</div>

</body>
</html>
```